Community coffee table book/quiz book

I need a couple of things for my book:
- Book cover (Title: "1000 gåter om Bakkeskog")
- "Cover pages" for each chapter of the book (15-16 chapters)
- "Watermark" or background design for all the pages of the book.
- A cover image for the book's Kvitre page.
- Design of a paper "belt"

The book:
The book will consist of about 200+ pages with ten questions on one page and ten answers on the next.

The name of the book is "1000 gåter om Bakkeskog" which means 1000 questions about Fyllingsdalen (Fyllingsdalen is a suburb of the city Bergen in Norway). Author is Helge Dyrnes.
The questions in the book are grouped in chapters like:
History
Facts
Schools
Businesses
People/profiles
Sport
Culture
Buildings/Landmarks/Sculptures
The different areas of the suburb
The city
Language/expressions
Nature
The names of the chapters are not set, so it would be good to have the option to change the title of the pages without having to contact the designer (maybe by adding the text on top of the cover page?). I therefore suggest that these images are without text.
The book size is 18X18 cm.

The chapter cover pages:
The book will basically consist of text. Ten questions on one page, and ten questions on the next. Visually it will be quite "boring" to look at. I would therefore like to have a chapter cover page for each chapter, preferable in colour.

Water mark:
To avoid having a book full of white pages with limited amount of text I thought of having some kind of design on each page. I do not know how this should be done, but maybe it is possible to create some kind of background image or watermark image with similar design as the book cover and the chapter covers?

The Kvitre cover image:
This should be the same as, or similar to, the book cover.
I believe the optimal size is 828px x 315px?

Paper "belt":
The book is to be sold for charity. The receiver of the money is the local sports club. I would like to have the book "wrapped in a 5-6 cm wide paper belt with the logo of the sports club (please see logo and colours here: http://www.ilvarnolia.no). I do not think that the book cover itself should have the sports club's color (purple), but maybe the paper band could? (Again: YOU are the designer)

Photos:
I reckon you would like some photos for both the book cover and the chapter covers. I will of course do the best I can to provide these photos when I have selected a designer. I the meantime

Target Market(s)

Target market is middle clas men and women 35+ from the geographical area Fyllingsdalen.

Industry/Entity Type

Community

Font styles to use
Serif
Sans Serif

Requirements
Must have
• The book will be sold by children on doors. The buyers will probably take a look briefly through the book and then decide if they are going to buy.
• It is important that they like the question types, categories and some of the actual questions they read. But it is also important that they like the look of the book. Therefore the book cover and the chapter cover pages must be appealing enough for the buyers to want this book on theor coffee table.
Nice to have
• I have uploaded a short video clip to Youtube (https://www.klipvista.example/watch?v=qt7Rmx2Lpaw). This a promo clip from Moravel Kids. I felt inspired when I saw it and thought that backgrounds like the ones used in the promo could also be used as backgrounds for each chapter's cover pages. Maybe different colour for each chapter? Screenshots from the clip is uploaded below.
• Then again: Maybe I am an idiot? YOU are the designer :-)
Should not have
• There has been some rivalry between two sportsclubs in the region after the clubs was merged a couple of years ago. I therefore believe we should therefore try avoid both the old clubs' colours (blue&yellow and green) and the new club's colour (purple).

```html
<!DOCTYPE html>
<html lang="no">
<head>
<meta charset="utf-8">
<title>1000 gåter om Bakkeskog – design board</title>
<link rel="stylesheet" href="https://fonts.googleapis.com/css2?family=Arimo:wght@400;700&family=Russo+One&display=swap">
<style>
  :root {
    --ink: #000000;
    --paper: #ffffff;
    --band-grey: #a9a9a9;
    --band-light: #cfcfcf;
    --sky-magenta: #c21fd6;
    --sky-violet: #7a1fa8;
    --sunset-orange: #f07a1e;
    --sunset-red: #c8201a;
    --night: #0b0508;
    --mono-light: #d9d9d9;
    --mono-mid: #7d7d7d;
    --mono-dark: #111111;
    --title-lilac: #b98ad6;
    --belt-grey: #c9c9c9;
    --belt-edge: #9e9e9e;
    --club-blue: #3a4f9e;
    --stage-grey: #e6e6e6;
  }
  * { margin: 0; padding: 0; box-sizing: border-box; }
  html, body { width: 849px; height: 1200px; overflow: hidden; background: var(--paper); }
  body { position: relative; font-family: "Arimo", Arial, sans-serif; color: var(--ink); }

  .board-heading {
    position: absolute; left: 52px; top: 18px;
    font-size: 57px; font-weight: 400; letter-spacing: 1px; line-height: 1;
  }

  .photo-mono {
    position: absolute; left: 51px; top: 104px; width: 333px; height: 335px;
    background: linear-gradient(180deg, var(--mono-dark) 0%, var(--mono-mid) 20%, var(--mono-light) 45%, var(--mono-mid) 60%, #f2f2f2 64%, var(--mono-dark) 70%, #000 100%);
  }

  .book-cover {
    position: absolute; left: 410px; top: 106px; width: 333px; height: 335px; overflow: hidden;
    background: linear-gradient(180deg, var(--night) 0%, var(--sky-violet) 12%, var(--sky-magenta) 30%, #e05ab0 48%, var(--sunset-orange) 62%, var(--sunset-red) 74%, var(--night) 84%, #000 100%);
  }
  .cover-title { position: absolute; left: 0; top: 98px; width: 100%; font-family: "Russo One", "Arimo", sans-serif; }
  .cover-number {
    display: block; margin-left: 58px; font-size: 74px; line-height: 1; letter-spacing: 6px;
    color: var(--title-lilac); -webkit-text-stroke: 2px #6a2d86;
  }
  .cover-sub {
    display: block; margin-left: 76px; margin-top: 6px; font-size: 28px; line-height: 1; color: #fff2f2;
  }
  .cover-place {
    display: block; margin-left: 40px; margin-top: 6px; padding: 2px 6px; width: fit-content;
    font-size: 30px; line-height: 1; letter-spacing: 3px; color: var(--paper);
    background: rgba(0,0,0,0.35);
  }

  .page-watermark {
    position: absolute; left: 56px; top: 473px; width: 340px; height: 342px;
    background: var(--paper); box-shadow: 3px 4px 6px rgba(0,0,0,0.45);
  }
  .page-author {
    position: absolute; left: 0; top: 19px; width: 100%; height: 14px;
    background: var(--band-light); color: #6d6d6d; font-size: 12px; line-height: 14px; text-align: center;
  }
  .page-title {
    position: absolute; left: 0; top: 40px; width: 100%; height: 28px;
    background: var(--band-grey); color: var(--paper); font-size: 21px; line-height: 28px; text-align: center;
  }
  .page-label {
    position: absolute; left: 0; top: 150px; width: 100%; text-align: center; font-size: 43px; line-height: 1;
  }
  .page-figure {
    position: absolute; left: 8px; top: 258px; width: 36px; height: 64px;
    background: linear-gradient(180deg, #eeeeee, #dcdcdc); border-radius: 14px 14px 4px 4px;
  }
  .page-foot { position: absolute; left: 0; bottom: 14px; width: 100%; height: 8px; background: var(--band-light); }

  .belt { position: absolute; left: 445px; top: 470px; width: 280px; height: 330px; }
  .belt-band { fill: url(#beltShade); stroke: var(--belt-edge); stroke-width: 1; }
  .belt-mark { fill: var(--club-blue); }
  .belt-name { font-family: "Arimo", sans-serif; font-size: 9px; fill: var(--club-blue); }
  .belt-heading {
    position: absolute; left: 566px; top: 482px; font-size: 55px; line-height: 1.08; text-align: right;
  }

  .social-stage {
    position: absolute; left: 56px; top: 838px; width: 690px; height: 334px;
    background: linear-gradient(180deg, #f7f7f7, var(--stage-grey));
  }
  .social-label { position: absolute; left: 14px; top: 12px; font-size: 26px; line-height: 1; }
  .social-cover {
    position: absolute; left: 30px; top: 56px; width: 630px; height: 240px; display: flex; overflow: hidden;
  }
  .social-cover .cover-colour {
    position: relative; width: 60%; height: 100%;
    background: linear-gradient(180deg, var(--night) 0%, var(--sky-violet) 12%, var(--sky-magenta) 30%, #e05ab0 48%, var(--sunset-orange) 62%, var(--sunset-red) 74%, var(--night) 84%, #000 100%);
  }
  .social-cover .cover-mono {
    width: 40%; height: 100%;
    background: linear-gradient(180deg, var(--mono-dark) 0%, var(--mono-mid) 20%, var(--mono-light) 45%, var(--mono-mid) 60%, #f2f2f2 64%, var(--mono-dark) 70%, #000 100%);
  }
  .social-title { position: absolute; left: 40px; top: 52px; font-family: "Russo One", "Arimo", sans-serif; }
  .social-title .cover-number { margin-left: 20px; font-size: 60px; }
  .social-title .cover-sub { margin-left: 34px; font-size: 24px; }
  .social-title .cover-place { margin-left: 0; font-size: 26px; }
</style>
</head>
<body>
  <h1 class="board-heading">BOOK COVER DESIGN</h1>

  <div class="photo-mono" role="img" aria-label="Black and white photograph of a cloudy sky over a dark landscape and water"></div>

  <div class="book-cover" role="img" aria-label="Book cover: coloured sunset photograph of a winding road with a child standing by it">
    <div class="cover-title">
      <span class="cover-number">1000</span>
      <span class="cover-sub">gåter om</span>
      <span class="cover-place">BAKKESKOG</span>
    </div>
  </div>

  <div class="page-watermark">
    <div class="page-author">Author's Name</div>
    <div class="page-title">1000 gåter om Bakkeskog</div>
    <div class="page-label">WATERMARK</div>
    <div class="page-figure" role="img" aria-label="Faint silhouette of a child"></div>
    <div class="page-foot"></div>
  </div>

  <svg class="belt" viewBox="0 0 280 330" aria-label="Paper belt with sports club name">
    <defs>
      <linearGradient id="beltShade" x1="0" y1="0" x2="1" y2="0">
        <stop offset="0" style="stop-color:#f4f4f4"/>
        <stop offset="0.5" style="stop-color:var(--belt-grey)"/>
        <stop offset="1" style="stop-color:#e8e8e8"/>
      </linearGradient>
    </defs>
    <path class="belt-band" d="M0 20 L28 0 C90 110 170 220 270 300 L252 322 C150 240 68 130 0 20 Z"/>
    <circle class="belt-mark" cx="30" cy="30" r="13"/>
    <text class="belt-name" x="48" y="56" transform="rotate(52 48 56)">IL Varnolia</text>
  </svg>
  <div class="belt-heading">BOOK<br>TAPE</div>

  <div class="social-stage">
    <div class="social-label">KVITRE COVER</div>
    <div class="social-cover">
      <div class="cover-colour" role="img" aria-label="Sunset photograph of a winding road with a child standing by it">
        <div class="social-title">
          <span class="cover-number">1000</span>
          <span class="cover-sub">gåter om</span>
          <span class="cover-place">BAKKESKOG</span>
        </div>
      </div>
      <div class="cover-mono" role="img" aria-label="Black and white photograph of a cloudy sky over a dark landscape"></div>
    </div>
  </div>
</body>
</html>
```